One Page Sales Flyer for Wireless Survey- Computer Hardware

I want a designer to create a one page 4 color sales slick to be given to our sales team to sell to the end customers. I would like a visual picture of a heat map so vornix "heat map wireless" to get an idea of how that image should look.

```html
<!DOCTYPE html>
<html lang="en">
<head>
<meta charset="utf-8">
<title>Corvane – Wireless Site Survey Sales Flyer</title>
<link href="https://fonts.googleapis.com/css2?family=Exo+2:wght@300;400;500;600&family=Roboto+Condensed:wght@400;700&display=swap" rel="stylesheet">
<style>
  :root {
    --page-bg: #e4e5e8;
    --brand-blue: #1463bb;
    --brand-blue-light: #3fa9f5;
    --heading-blue: #1a6fc4;
    --ink: #2a2a2a;
    --body-ink: #333333;
    --panel-grey: #f0f0f0;
    --rule-grey: #c9c9c9;
    --footer-grey: #5f5f5f;
    --num-1: #e1262c;
    --num-2: #ec5424;
    --num-3: #f07d2a;
    --num-4: #f59b2b;
    --white: #ffffff;
  }
  * { box-sizing: border-box; margin: 0; padding: 0; }
  html, body { width: 1200px; height: 1200px; overflow: hidden; }
  body { background: var(--page-bg); position: relative; font-family: "Roboto Condensed", sans-serif; }

  .flyer {
    position: absolute; left: 159px; top: 30px;
    width: 882px; height: 1140px;
    background: var(--white);
    box-shadow: 0 6px 24px rgba(0,0,0,.18);
    overflow: hidden;
  }

  .hero-photo {
    position: absolute; left: 0; top: 0; width: 558px; height: 517px;
    background:
      radial-gradient(ellipse at 30% 45%, #f1b64a 0%, #d9762e 18%, transparent 40%),
      radial-gradient(ellipse at 70% 40%, #b9c7cf 0%, transparent 55%),
      linear-gradient(160deg, #6f7478 0%, #d8dadb 35%, #eef0f0 60%, #c7b8a8 100%);
  }

  .audience-panel {
    position: absolute; left: 558px; top: 0; width: 324px; height: 517px;
    background: var(--brand-blue); color: var(--white);
    font-family: "Exo 2", sans-serif;
  }
  .brand { position: absolute; display: flex; align-items: center; gap: 14px; }
  .brand-mark { width: 54px; height: 54px; border: 3px solid var(--white); border-radius: 6px; }
  .brand-name { font-family: "Exo 2", sans-serif; font-weight: 400; color: var(--white); letter-spacing: 1px; }
  .audience-panel .brand { left: 74px; top: 53px; }
  .audience-panel .brand-name { font-size: 27px; }

  .audience-title {
    position: absolute; left: 77px; top: 146px;
    font-weight: 300; font-size: 24px; line-height: 31px;
    color: var(--brand-blue-light); text-transform: uppercase;
  }
  .audience-list { position: absolute; left: 60px; top: 236px; list-style: none; }
  .audience-list li {
    font-size: 20px; font-weight: 500; line-height: 24.5px;
    padding-left: 17px; position: relative;
  }
  .audience-list li::before {
    content: ""; position: absolute; left: 0; top: 8px;
    border-left: 7px solid var(--brand-blue-light);
    border-top: 4.5px solid transparent; border-bottom: 4.5px solid transparent;
  }

  .story { position: absolute; left: 69px; top: 517px; width: 432px; }
  .headline {
    margin-top: 31px;
    font-family: "Exo 2", sans-serif; font-weight: 300;
    font-size: 42px; line-height: 49px; color: var(--ink); letter-spacing: .3px;
  }
  .headline strong { font-weight: 500; }
  .question {
    font-family: "Exo 2", sans-serif; font-weight: 500;
    font-size: 21px; color: var(--heading-blue);
  }
  .story .q1 { margin-top: 26px; }
  .story .q2 { margin-top: 24px; }
  .answer {
    margin-top: 6px; font-size: 14px; line-height: 19.5px;
    color: var(--body-ink); text-align: justify;
  }

  .reasons {
    position: absolute; left: 558px; top: 517px; width: 324px; height: 515px;
    background: var(--panel-grey);
  }
  .reasons-title {
    position: absolute; left: 21px; top: 32px;
    font-family: "Exo 2", sans-serif; font-size: 20px; font-weight: 400; color: var(--ink);
  }
  .reason { position: absolute; left: 0; width: 324px; }
  .reason-num {
    position: absolute; left: 22px; top: -6px;
    font-family: "Exo 2", sans-serif; font-weight: 600; font-size: 62px; line-height: 62px;
  }
  .reason-text {
    position: absolute; left: 74px; width: 224px;
    font-size: 14px; line-height: 19.3px; color: var(--body-ink);
  }
  .reason-rule { position: absolute; left: 4px; width: 270px; height: 1px; background: var(--rule-grey); }

  .footer-contact {
    position: absolute; left: 0; top: 1032px; width: 558px; height: 108px;
    background: var(--footer-grey); color: var(--white);
  }
  .footer-contact .brand { left: 38px; top: 18px; flex-direction: column; gap: 6px; }
  .footer-contact .brand-mark { width: 44px; height: 44px; }
  .footer-contact .brand-name { font-size: 19px; }
  .address { position: absolute; left: 170px; top: 27px; font-family: "Exo 2", sans-serif; font-size: 16px; line-height: 19px; }
  .address b { font-weight: 600; }
  .address .email { color: #cfcfcf; font-weight: 300; }
  .footnote { position: absolute; left: 170px; top: 81px; font-size: 10.5px; }

  .footer-cta {
    position: absolute; left: 558px; top: 1032px; width: 324px; height: 108px;
    background: linear-gradient(180deg, #2b7bd0 0%, var(--brand-blue) 8%);
    color: var(--white); text-align: center; font-family: "Exo 2", sans-serif;
  }
  .phone { margin-top: 18px; font-size: 33px; font-weight: 300; letter-spacing: .5px; }
  .web { font-size: 21px; font-weight: 400; }
</style>
</head>
<body>
  <article class="flyer">
    <div class="hero-photo" role="img" aria-label="Photo of a person typing on a laptop that shows a colour wireless signal heat map over an office floor plan"></div>

    <aside class="audience-panel">
      <div class="brand">
        <span class="brand-mark"></span>
        <span class="brand-name">CORVANE</span>
      </div>
      <h2 class="audience-title">Target<br>Customers</h2>
      <ul class="audience-list">
        <li>Distributors</li>
        <li>Warehouses</li>
        <li>SLED</li>
        <li>K-12</li>
        <li>Medical / Hospitals</li>
        <li>Enterprise F1000</li>
        <li>Sports Venues</li>
        <li>Stadiums</li>
        <li>Hotels</li>
        <li>Retail stores</li>
      </ul>
    </aside>

    <section class="story">
      <h1 class="headline"><strong>Increase Hardware &amp; Services</strong> Spend with Wireless Site Surveys</h1>
      <h3 class="question q1">What is a wireless site survey or heat map?</h3>
      <p class="answer">A wireless site survey is a compilation of reports showing a visual representation of health of your wireless network. This does not only show how strong or weak a wireless signal is in any location it also helps aid in channel and placement to ensure maximum stable data rates are archived even where the single appears strong.</p>
      <h3 class="question q2">Why do customers need a site survey?</h3>
      <p class="answer">Any variety of factors can contribute to an unhealthy wireless network (electrical, motors, materials used in construction, distance, neighboring wireless networks, etc.) and traditional methods that use only blueprints and a computer program to show signal strength have shown to be ineffective.</p>
    </section>

    <section class="reasons">
      <h2 class="reasons-title">Why should they use you?</h2>
      <div class="reason" style="top:79px">
        <span class="reason-num" style="color:var(--num-1)">1</span>
        <p class="reason-text">42% of businesses report some issues with wireless connectivity and acknowledge its effect on the bottom line*</p>
      </div>
      <div class="reason-rule" style="top:165px"></div>
      <div class="reason" style="top:187px">
        <span class="reason-num" style="color:var(--num-2)">2</span>
        <p class="reason-text">Most of these problems are solved through either fine tuning the current equipment (managed services) or purchasing new equipment (incremental sales) of which you can provide both</p>
      </div>
      <div class="reason-rule" style="top:317px"></div>
      <div class="reason" style="top:338px">
        <span class="reason-num" style="color:var(--num-3)">3</span>
        <p class="reason-text">Being a one-stop shop for all your customer's IT needs prevents them from needing additional vendors</p>
      </div>
      <div class="reason-rule" style="top:415px"></div>
      <div class="reason" style="top:430px">
        <span class="reason-num" style="color:var(--num-4)">4</span>
        <p class="reason-text">The increase of IoT (Internet of things) and BYOD (Bring Your Own Device)</p>
      </div>
    </section>

    <footer class="footer-contact">
      <div class="brand">
        <span class="brand-mark"></span>
        <span class="brand-name">CORVANE</span>
      </div>
      <p class="address"><b>Corvane</b> 410 Harbor Loop, Fairview, CA 92000<br><span class="email">info@corvanetech.com</span></p>
      <p class="footnote">*Veltrane Research. "Connectivity in the Modern Enterprise". June 2017</p>
    </footer>
    <div class="footer-cta">
      <p class="phone">555-014-2270</p>
      <p class="web">www.corvanetech.com</p>
    </div>
  </article>
</body>
</html>
```